Stylish Business Card for Modern hair salon

I need a simple business card design using our salon logo and colours that are in the logo. We service clients of all ages but predominantly those in the 18 to 55 age range. We have a young staff and are looking to have a card that will present a modern and clean image that represents who we are. The card should be in black and white same as our logo. Minimal use of other colours is allowed.

Industry/Entity Type

Hair And Beauty

Contact Information for Business Card

The design should have the following information
salon name - TZ Hair Studio
address - 2957 Fernbrook Rd.W. Mississauga, ON L8R3P2
phone - 905 641-2087
website - tzhairexample.ca
instagram - tz.hairstudio
twitter - @TZ_HairStudio

Colors
000000
ffffff
474747

Requirements
Must have
• simple design, salon name, address, phone, website, instagram, twitter info
• Back of card should have the following:
• YOUR NEXT APPOINTMENT
• DATE
• TIME
Nice to have
• simple design, clear to see and read,
• predominantly black and white colour, minimal use of other colours is ok
Should not have
• many colours, various fonts

```html
<!DOCTYPE html>
<html lang="en">
<head>
<meta charset="utf-8">
<title>TZ Hair Studio – Business Card</title>
<link rel="stylesheet" href="https://fonts.googleapis.com/css2?family=Questrial&display=swap">
<style>
  :root {
    --ink: #000000;
    --paper: #ffffff;
    --graphite: #474747;
    --silver: #b9b9b9;
    --backdrop: #e6e6e6;
  }
  * { margin: 0; padding: 0; box-sizing: border-box; }
  html, body {
    width: 1200px; height: 780px; overflow: hidden;
    background: var(--backdrop);
    font-family: "Questrial", "Century Gothic", sans-serif;
  }
  .canvas { position: relative; width: 1200px; height: 780px; }

  .card {
    position: absolute; top: 230px;
    width: 525px; height: 300px;
    box-shadow: 0 6px 18px rgba(0,0,0,0.18);
  }

  /* Front */
  .card-front { left: 50px; background: var(--ink); }
  .card-front .brand {
    position: absolute; left: 0; right: 0; top: 50%;
    transform: translateY(-50%);
    display: flex; align-items: center; justify-content: center; gap: 14px;
    color: var(--silver);
    font-size: 40px; letter-spacing: 3px;
  }
  .brand-mark { width: 14px; height: 14px; background: currentColor; }

  /* Back */
  .card-back { left: 625px; background: var(--paper); color: var(--ink); }
  .card-back .brand {
    position: absolute; left: 28px; top: 70px; width: 230px;
    font-size: 28px; letter-spacing: 1.5px; text-align: center;
    color: var(--ink);
  }
  .card-back .divider {
    position: absolute; left: 272px; top: 34px;
    width: 1px; height: 150px; background: var(--ink);
  }
  .contact {
    position: absolute; left: 290px; top: 40px;
    font-size: 14px; line-height: 19px; list-style: none;
  }
  .contact .address { margin-bottom: 4px; }
  .contact-item { display: flex; align-items: center; gap: 7px; }
  .contact-icon { width: 13px; height: 13px; flex: none; }
  .dot { width: 11px; height: 11px; border-radius: 50%; background: var(--ink); flex: none; margin: 0 1px; }

  .appointment {
    position: absolute; left: 28px; right: 28px; top: 200px;
    font-size: 13px; letter-spacing: 0.5px; color: var(--ink);
  }
  .field { position: absolute; display: flex; align-items: flex-end; gap: 6px; }
  .field .rule { border-bottom: 1px solid var(--ink); height: 1px; }
  .field-date { left: 0; top: 0; }
  .field-date .rule { width: 150px; }
  .appointment-title { position: absolute; left: 200px; top: 2px; }
  .field-time { left: 240px; top: 48px; }
  .field-time .rule { width: 175px; }
</style>
</head>
<body>
<main class="canvas">
  <section class="card card-front" aria-label="Card front">
    <div class="brand"><span class="brand-mark"></span><span>TZ Hair Studio</span></div>
  </section>

  <section class="card card-back" aria-label="Card back">
    <div class="brand">TZ Hair Studio</div>
    <div class="divider"></div>
    <ul class="contact">
      <li class="address">2957 Fernbrook Rd.<br>W. Mississauga, ON L8R3P2</li>
      <li class="contact-item">
        <svg class="contact-icon" viewBox="0 0 24 24" aria-hidden="true"><circle cx="12" cy="12" r="12" fill="#000"/><path d="M8 6.5l2 0 1 3-1.5 1a7 7 0 0 0 4 4l1-1.5 3 1v2a1.5 1.5 0 0 1-1.5 1.5A10 10 0 0 1 6.5 8 1.5 1.5 0 0 1 8 6.5z" fill="#fff"/></svg>
        <span>905 641-2087</span>
      </li>
      <li class="contact-item"><span class="dot"></span><span>tzhairexample.ca</span></li>
      <li class="contact-item"><span class="dot"></span><span>tz.hairstudio</span></li>
      <li class="contact-item"><span class="dot"></span><span>@TZ_HairStudio</span></li>
    </ul>

    <div class="appointment">
      <div class="field field-date"><span>DATE</span><span class="rule"></span></div>
      <div class="appointment-title">YOUR NEXT APPOINTMENT</div>
      <div class="field field-time"><span>TIME</span><span class="rule"></span></div>
    </div>
  </section>
</main>
</body>
</html>
```